My colors are BLACK, WHITE AND RED. I want something super professional but feminine and a bit sassy. My original logo is gold and black, I would like to see the crown in red (still with gradient) . I have a suggested layout in the files but am totally open to fresh ideas. I'm torn about having a little crown on the front as well as large logo on the back.

Target Market(s)

People buying high end houses

Font styles to use
Serif
Sans Serif

Requirements
Must have
• all the verbiage and text needed is on the business card in the files.
Nice to have
• classy, pretty, elegant, business like
Should not have
• cheesy, guady, boring

```html
<!DOCTYPE html>
<html lang="en">
<head>
<meta charset="utf-8">
<title>Vivienne Ashford – Business Card</title>
<link href="https://fonts.googleapis.com/css2?family=Open+Sans:wght@300;400;600&display=swap" rel="stylesheet">
<style>
  :root {
    --backdrop: #2e2a27;
    --card: #c8c8c8;
    --card-shade: #bdbdbd;
    --ink: #2a2a2a;
    --ink-soft: #3a3a3a;
    --accent-red: #e0222b;
    --emboss: #a9a9a9;
    --photo-dark: #3b3b3d;
    --photo-warm: #b8672f;
  }
  * { box-sizing: border-box; margin: 0; padding: 0; }
  html, body { width: 1200px; height: 672px; overflow: hidden; }
  body {
    background: var(--backdrop);
    font-family: "Open Sans", Arial, sans-serif;
    display: flex;
    align-items: center;
    justify-content: center;
    gap: 46px;
  }
  .card {
    position: relative;
    width: 530px;
    height: 303px;
    background: var(--card);
    box-shadow: 0 10px 24px rgba(0,0,0,0.45);
    overflow: hidden;
  }

  /* Front */
  .card-front .identity {
    position: absolute;
    left: 34px;
    top: 30px;
  }
  .agent-name {
    font-weight: 300;
    font-size: 26px;
    color: var(--ink);
    letter-spacing: 0.2px;
  }
  .agent-title {
    font-weight: 600;
    font-size: 12.5px;
    color: var(--accent-red);
    margin-top: 2px;
  }
  .credentials {
    list-style: none;
    margin-top: 4px;
    font-size: 12.5px;
    line-height: 1.38;
    color: var(--ink-soft);
  }
  .contact {
    position: absolute;
    left: 34px;
    bottom: 34px;
    font-size: 12.5px;
    color: var(--ink-soft);
    list-style: none;
    line-height: 1.75;
  }
  .contact .brokerage { font-weight: 600; letter-spacing: 0.3px; margin-bottom: 4px; }
  .contact li { display: flex; align-items: center; gap: 8px; }
  .contact-icon { width: 12px; height: 12px; flex: none; }
  .agent-portrait {
    position: absolute;
    right: 24px;
    bottom: 0;
    width: 210px;
    height: 236px;
    border-radius: 105px 105px 0 0;
    background: linear-gradient(160deg, var(--photo-warm) 0%, #8a5736 40%, var(--photo-dark) 75%);
  }

  /* Back */
  .card-back {
    display: flex;
    align-items: center;
    justify-content: center;
    background: linear-gradient(135deg, var(--card) 0%, var(--card-shade) 100%);
  }
  .monogram-wordmark {
    display: flex;
    align-items: center;
    gap: 14px;
    font-weight: 300;
    font-size: 24px;
    letter-spacing: 7px;
    color: var(--emboss);
    text-transform: uppercase;
  }
  .monogram-wordmark .mark-square {
    width: 10px;
    height: 10px;
    background: var(--emboss);
  }
</style>
</head>
<body>

  <section class="card card-front">
    <div class="identity">
      <h1 class="agent-name">Vivienne Ashford</h1>
      <p class="agent-title">Real Estate Agent</p>
      <ul class="credentials">
        <li>Certified Mountain Area Specialist</li>
        <li>Certified Luxury Home Marketing Specialist</li>
        <li>Certified Negotiation Expert</li>
      </ul>
    </div>

    <ul class="contact">
      <li class="brokerage">SUMMIT ALLIANCE</li>
      <li>
        <svg class="contact-icon" viewBox="0 0 12 12" aria-hidden="true">
          <rect width="12" height="12" rx="1.5" fill="var(--accent-red)"/>
          <path d="M3.4 2.6 L5 4.4 L4.2 5.3 Q5 6.9 6.7 7.8 L7.6 7 L9.4 8.6 L8.4 9.6 Q4.6 9 2.4 3.6 Z" fill="#fff"/>
        </svg>
        <span>555-014-2287</span>
      </li>
      <li>
        <svg class="contact-icon" viewBox="0 0 12 12" aria-hidden="true">
          <rect width="12" height="12" rx="1.5" fill="var(--accent-red)"/>
          <rect x="2.2" y="3.4" width="7.6" height="5.2" fill="none" stroke="#fff" stroke-width="0.9"/>
          <path d="M2.2 3.4 L6 6.4 L9.8 3.4" fill="none" stroke="#fff" stroke-width="0.9"/>
        </svg>
        <span>vashford@summitrealty.net</span>
      </li>
    </ul>

    <div class="agent-portrait" role="img" aria-label="Portrait photo of the agent in a dark blazer"></div>
  </section>

  <section class="card card-back">
    <div class="monogram-wordmark">
      <span class="mark-square" aria-hidden="true"></span>
      <span>Vivienne Ashford</span>
    </div>
  </section>

</body>
</html>
```